A Leisure SPA Plaza Hotel needs Creative VIP Cards Design

We need VIP Cards Design for a SPA Plaza Hotel, This leisure SPA plaza hotel have multiple sub projects, such as leisure hotel room, large buffet restaurant, swimming pool, theatrical performances, sauna bath, massage, SPA, Tea bar, 3D cinema, KTV rooms, chess room, Internet cafes , art appreciation, children's Castle, Korean geothermal, table tennis, billiard room, GYM and other entertainments.
We need Three creative VIP Card design for 3 different level:
1. Golden Card
2. Platinum Card
3. Diamond Card
Attached, Please find the LOGO file and some sample, we new design with much better look than those samples.

```html
<!DOCTYPE html>
<html lang="en">
<head>
<meta charset="utf-8">
<title>Coral Bay Leisure Plaza – Membership Cards</title>
<link rel="stylesheet" href="https://fonts.googleapis.com/css2?family=Raleway:wght@200;300;400;700&family=Open+Sans:wght@400&display=swap">
<style>
:root{
  --page-light:#e2e2e2;
  --page-dark:#a9a9a9;
  --gold:#e6dc7a;
  --gold-deep:#b8a948;
  --silver:#eef0f2;
  --silver-deep:#b9bcc0;
  --gold-card-a:#2e2e2e;
  --gold-card-b:#0d0d0d;
  --diamond-card-a:#1d2a4c;
  --diamond-card-b:#0a1124;
  --platinum-card-a:#5e1a30;
  --platinum-card-b:#210a12;
  --stripe-a:#f4f4f4;
  --stripe-b:#dedede;
}
*{margin:0;padding:0;box-sizing:border-box}
html,body{width:1200px;height:915px;overflow:hidden}
body{
  position:relative;
  background:radial-gradient(ellipse at 50% 40%,var(--page-light) 0%,var(--page-dark) 100%);
  font-family:"Raleway",sans-serif;
}
.card{
  position:absolute;width:522px;height:330px;border-radius:22px;overflow:hidden;
  box-shadow:0 4px 10px rgba(0,0,0,.35);
}
.card-texture{position:absolute;inset:0}
.card--gold .card-texture{background:linear-gradient(135deg,var(--gold-card-a) 0%,var(--gold-card-b) 55%,var(--gold-card-a) 100%)}
.card--diamond .card-texture{background:linear-gradient(135deg,var(--diamond-card-a) 0%,var(--diamond-card-b) 60%,var(--diamond-card-a) 100%)}
.card--platinum .card-texture{background:linear-gradient(135deg,var(--platinum-card-a) 0%,var(--platinum-card-b) 60%,var(--platinum-card-a) 100%)}

.front-top{top:92px;left:67px}
.back-top{top:113px;left:611px}
.front-bottom-left{top:470px;left:67px;width:525px;height:331px}
.front-bottom-right{top:494px;left:611px}

.brand{
  position:absolute;top:72px;left:0;right:0;
  display:flex;align-items:center;justify-content:center;gap:10px;
  font-weight:400;font-size:20px;letter-spacing:.5px;
}
.brand-dot{width:14px;height:14px;border-radius:50%}
.tier{position:absolute;left:0;right:0;top:160px;text-align:center}
.tier-name{
  display:block;font-weight:200;font-size:66px;line-height:1;letter-spacing:1px;
}
.tier-label{
  display:flex;align-items:center;justify-content:center;gap:10px;margin-top:4px;
  font-weight:700;font-size:26px;letter-spacing:7px;
}
.tier-label::before,.tier-label::after{content:"";display:block;width:64px;height:2px;background:currentColor}
.serial{position:absolute;right:48px;bottom:36px;font-family:"Open Sans",sans-serif;font-size:22px}

.card--gold .brand,.card--gold .tier,.card--gold .serial{color:var(--gold)}
.card--gold .brand-dot{background:var(--gold-deep)}
.card--diamond .brand,.card--diamond .tier,.card--diamond .serial{color:var(--silver)}
.card--diamond .brand-dot,.card--platinum .brand-dot{background:var(--silver-deep)}
.card--platinum .brand,.card--platinum .tier,.card--platinum .serial{color:var(--silver-deep)}
.card--platinum .tier-name{color:var(--silver)}

.back{color:var(--gold);font-family:"Open Sans",sans-serif;text-align:center}
.back-title{position:absolute;top:48px;left:0;right:0;font-size:23px;letter-spacing:.5px}
.signature-strip{
  position:absolute;top:97px;left:99px;width:320px;height:52px;border-radius:8px;
  background:repeating-linear-gradient(135deg,var(--stripe-a) 0 3px,var(--stripe-b) 3px 5px);
}
.back-terms{position:absolute;top:168px;left:0;right:0;font-size:15.5px;line-height:21px}
.back-contact{position:absolute;top:264px;left:0;right:0;font-size:15px}
.back-contact strong{font-weight:400;font-size:23px;margin-left:4px}
</style>
</head>
<body>

<section class="card card--gold front-top">
  <div class="card-texture" role="img" aria-label="Dark faceted geometric background"></div>
  <div class="brand"><span class="brand-dot"></span>Coral Bay Leisure Plaza</div>
  <div class="tier"><span class="tier-name">GOLDEN</span><span class="tier-label">CARD</span></div>
  <div class="serial">00273</div>
</section>

<section class="card card--gold back back-top">
  <div class="card-texture" role="img" aria-label="Dark faceted geometric background"></div>
  <h2 class="back-title" style="font-weight:400">AUTHORIZED SIGNATURE</h2>
  <div class="signature-strip"></div>
  <p class="back-terms">Please show your membership card when you check out.<br>Signature and use of this card confirms the acceptance<br>of the Terms and Conditions of Membership.</p>
  <p class="back-contact">Call us:<strong>4001357246</strong></p>
</section>

<section class="card card--diamond front-bottom-left">
  <div class="card-texture" role="img" aria-label="Navy faceted geometric background"></div>
  <div class="brand"><span class="brand-dot"></span>Coral Bay Leisure Plaza</div>
  <div class="tier"><span class="tier-name">DIAMOND</span><span class="tier-label">CARD</span></div>
  <div class="serial">00273</div>
</section>

<section class="card card--platinum front-bottom-right">
  <div class="card-texture" role="img" aria-label="Burgundy faceted geometric background"></div>
  <div class="brand"><span class="brand-dot"></span>Coral Bay Leisure Plaza</div>
  <div class="tier"><span class="tier-name">PLATINUM</span><span class="tier-label">CARD</span></div>
  <div class="serial">00273</div>
</section>

</body>
</html>
```